Law Firm Website
Innovative and Professional
Project: Law Firm Website
Law Firm Website - Law
Creative Brief
Law
www.tambelcounsel.com
Please see website.
Please see detailed instructions and images attached.
Modern
deep red as in the brastow site below
left side
http://www.brastow.com/
http://www.tmvg.co.ke/
Please see detailed instructions and suggested images in the attached docs.
vmorkin vmorkin
Comment on #60: At the bottom the phone and fax number should be lined up so the numbers are vertically aligned.
Here are a few more options for the family image: http://www.pixoravault.com/stock-illustration-50291736-family-tree-template.php?st=kq7f3d1 http://www.pixoravault.com/stock-photo-61834207-stone-figures-coastline.php?st=m82c5e0 http://www.pixoravault.com/stock-illustration-73920415-vintage-family-tree-with-golden-pictureholders-and-ribbons-dark-background.php?st=kq7f3d1
P.S. By the visa stamp, I mean the red visa stamp on the top right of the page.
We really like #60. We'd like to switch up one of the images. Specifically, could you switch the hands image with one of a family tree such as: http://www.framelundry.com/pic-82615094/stock-vector-family-tree-kinfolk.html?src=pQwErT7uYhGvBnM-ZxcvbN-5-28 or http://www.corvalimage.com/detail/illustration/portraits-on-family-tree-stock-graphic/38204917 (though I'm not sure green would look good with the existing colors) or a different image that you suggest? Also, can you try some options without the visa stamp on the right. We're not sure about that. Finally, please remove the Quick Contact page. We'd rather have people call or email rather than get in touch that way.
We can't star again, but we also like #31. Three stars.
A few more images: http://www.corvalimage.com/detail/photo/view-of-national-flag-from-harbor-pier-royalty-free-image/259403817 http://www.corvalimage.com/detail/photo/this-is-the-state-dome-during-the-anniversary-of-royalty-free-image/41958302
I do like design #38. For some reason am unable to star. I think the other designs have too many images that compete for attention. #38 is easy on the eyes, a little simpler, so I like that. I also like the white and black header and footing in #8. I know I said red, but that looks very sharp to me.
Please also remove the same-sex category from the home page. This should really be a separate page linked from the family immigration page.
Please see the following links for possible images for the main top image. I'm not liking the look of the green card, social security card and flag. Nor do I really like the airport scene, now that I see it on the page. I am also open to your suggestions on this main images. http://www.pixoravault.com/stock-photo-8351027-immigration.php?st=r4t9b2a http://www.pixoravault.com/stock-photo-27364019-grunge-harbor-monument.php?st=r4t9b2a http://www.pixoravault.com/stock-photo-6152934-grunge-harbor-monument.php?st=r4t9b2a http://www.pixoravault.com/stock-illustration-5930281-harbor-islet.php?st=w6e1k83

```html
<!DOCTYPE html>
<html lang="en">
<head>
<meta charset="utf-8">
<title>Tambel Law Office</title>
<link href="https://fonts.googleapis.com/css2?family=Arimo:ital,wght@0,400;0,700;1,700&display=swap" rel="stylesheet">
<style>
:root{
  --crimson:#a8173c;
  --crimson-dark:#8c1030;
  --crimson-light:#c2325a;
  --tab:#e9d9d6;
  --nav-active:#f3c98c;
  --gold:#f6c51b;
  --amber:#eea40f;
  --maroon:#7a1226;
  --page:#ffffff;
  --mist:#e6e6e6;
  --ink:#333333;
  --cream:#f6e9e2;
}
*{box-sizing:border-box;margin:0;padding:0}
html,body{width:1200px;height:1099px;overflow:hidden}
body{font-family:"Arimo",Arial,sans-serif;background:var(--page);color:var(--ink);position:relative}
.site-header{position:absolute;left:0;top:0;width:1200px;height:130px;background:linear-gradient(var(--crimson-light),var(--crimson) 60%,var(--crimson-dark))}
.brand{position:absolute;left:160px;top:14px;display:flex;align-items:center;gap:12px}
.brand-mark{width:104px;height:104px;border-radius:50%;border:3px solid var(--nav-active);display:flex;align-items:center;justify-content:center;text-align:center;color:var(--nav-active);font-size:15px;font-weight:700;line-height:1.2}
.call-tab{position:absolute;left:735px;top:0;width:300px;height:36px;background:var(--tab);border-radius:0 0 8px 8px;display:flex;align-items:center;justify-content:center;gap:10px;font-size:20px;color:var(--crimson);font-weight:700}
.call-tab svg{width:20px;height:20px}
.call-tab .label{font-weight:400;color:#a06060}
.main-nav{position:absolute;left:570px;top:60px;display:flex;gap:18px;list-style:none}
.main-nav a{display:block;padding:8px 16px;color:#fff;font-size:17px;text-decoration:none;border-radius:3px}
.main-nav a.active{background:var(--nav-active);color:var(--maroon)}
.stage{position:absolute;left:0;top:130px;width:1200px;height:470px;background:linear-gradient(var(--mist),#f6f6f6 75%,var(--page))}
.hero{position:absolute;left:141px;top:165px;width:924px;height:360px;background:#fff;padding:12px;box-shadow:0 18px 22px -14px rgba(0,0,0,.45)}
.hero-panel{position:relative;width:100%;height:100%;background:linear-gradient(110deg,var(--gold),var(--amber) 55%,#f3b62a);overflow:hidden}
.hero-text{position:absolute;left:51px;top:75px;width:400px;font-size:26px;line-height:33px;font-style:italic;font-weight:700;color:var(--maroon)}
.hero-art{position:absolute;right:0;top:0;width:440px;height:100%;background:linear-gradient(90deg,rgba(255,255,255,0),rgba(255,245,200,.55) 40%,rgba(90,40,10,.35))}
.hero-dots{position:absolute;right:40px;bottom:12px;display:flex;gap:8px}
.hero-dots span{width:10px;height:10px;border-radius:50%;background:#fff;opacity:.6}
.hero-dots span:first-child{background:var(--crimson);opacity:1}
.practice{position:absolute;top:615px;left:141px;width:924px;height:285px}
.card{position:absolute;top:0;height:285px;border:1px solid #d8d8d8;border-radius:8px;background:#fff;box-shadow:0 2px 6px rgba(0,0,0,.18);overflow:hidden}
.card-title{height:36px;margin:0 6px;background:var(--crimson);color:#fff;font-size:15px;font-weight:700;display:flex;align-items:center;justify-content:center;text-align:center;line-height:1.1;border-radius:0 0 6px 6px}
.card-image{height:120px;margin:8px 8px 0}
.card-text{padding:10px 10px;font-size:13px;line-height:17px;text-align:center;color:var(--ink)}
.site-footer{position:absolute;left:0;top:939px;width:1200px;height:160px;background:var(--crimson);color:var(--cream);text-align:center}
.footer-nav{display:flex;justify-content:center;gap:8px;list-style:none;margin-top:14px;font-size:13px}
.footer-nav li+li::before{content:"|";margin-right:8px}
.footer-copy{margin:10px auto 0;width:960px;font-size:11px;line-height:15px}
.payments{margin-top:10px;display:flex;justify-content:center;align-items:center;gap:14px;font-size:12px}
.pay{display:flex;align-items:center;gap:5px;font-weight:700;color:#fff}
.pay i{display:block;width:14px;height:14px;background:var(--cream)}
</style>
</head>
<body>
<header class="site-header">
  <div class="brand"><div class="brand-mark">Tambel<br>Law Office</div></div>
  <div class="call-tab">
    <svg viewBox="0 0 24 24"><path fill="currentColor" d="M6.6 10.8a15 15 0 0 0 6.6 6.6l2.2-2.2a1 1 0 0 1 1-.25 11.4 11.4 0 0 0 3.6.57 1 1 0 0 1 1 1V20a1 1 0 0 1-1 1A17 17 0 0 1 3 4a1 1 0 0 1 1-1h3.5a1 1 0 0 1 1 1c0 1.25.2 2.45.57 3.57a1 1 0 0 1-.25 1z"/></svg>
    <span class="label">Call Us Today</span><span>312-555-0148</span>
  </div>
  <ul class="main-nav">
    <li><a class="active" href="#">Home</a></li>
    <li><a href="#">About</a></li>
    <li><a href="#">Practice Areas</a></li>
    <li><a href="#">Immigration News</a></li>
    <li><a href="#">Contact us</a></li>
  </ul>
</header>

<div class="stage"></div>

<section class="hero">
  <div class="hero-panel">
    <p class="hero-text">The Tambel Law Office is an experienced U.S. immigration firm dedicated to serving individuals and businesses through the practice of immigration law.</p>
    <div class="hero-art" role="img" aria-label="Silhouette of a harbor monument statue over swirling golden light"></div>
    <div class="hero-dots"><span></span><span></span><span></span></div>
  </div>
</section>

<section class="practice">
  <article class="card" style="left:0;width:189px">
    <h2 class="card-title">Family Immigration Law</h2>
    <div class="card-image" role="img" aria-label="Family hands stacked together" style="background:linear-gradient(#d9b59a,#8a5a44)"></div>
    <p class="card-text">Green Cards, Immediate Relative Petitions, Special Visas, Fiancé Visas, Naturalization &amp; Citizenship, Hardship Waivers</p>
  </article>
  <article class="card" style="left:243px;width:192px">
    <h2 class="card-title">Business Immigration Law</h2>
    <div class="card-image" role="img" aria-label="Drawing of a businessman at a desk with paperwork" style="background:linear-gradient(#f0f0f0,#9a9a9a)"></div>
    <p class="card-text">H-1Bs, L-1s, PERM Labor Certifications, Employment Based Green Cards, Investor/Treaty Trader Visas</p>
  </article>
  <article class="card" style="left:483px;width:195px">
    <h2 class="card-title">Comprehensive Immigration Reform 2014</h2>
    <div class="card-image" role="img" aria-label="Question mark among reform notices" style="background:linear-gradient(#e4e4e4,#b8443e)"></div>
    <p class="card-text">Click Here for the Latest on Immigration Reform 2014!</p>
  </article>
  <article class="card" style="left:723px;width:201px">
    <h2 class="card-title">Same-Sex Couple Immigration</h2>
    <div class="card-image" role="img" aria-label="Rainbow flag waving" style="background:linear-gradient(#d33,#f90,#ee3,#3a3,#36c,#839)"></div>
    <p class="card-text">We Help Same-Sex Couples Navigate Recent Changes in Immigration Law</p>
  </article>
</section>

<footer class="site-footer">
  <ul class="footer-nav"><li>Home</li><li>About</li><li>Practice Areas</li><li>Immigration News</li><li>Contact us</li></ul>
  <p class="footer-copy">Tambel Law Office. All Rights Reserved | 45 Harlow Street, 4th Floor, Chicago, IL 60602 | 312-555-0148 |<br>The information on this website is for general information purposes only. Nothing on this or associated pages, documents, comments, answers, emails, or other communications should be taken as legal advice for any individual case or situation. This information on this website is not intended to create, and receipt or viewing of this information does not constitute, an attorney-client relationship.</p>
  <div class="payments"><span>We accept the following payment methods:</span><span class="pay">Cash <i></i></span><span class="pay">Check <i></i></span></div>
</footer>
</body>
</html>
```